web site update

I want to get a better website for a small high end remodeling and construction company
I currently have a web site but you will find that it is not good.
www.quenbrickhall.com
We are a high end construction / remodeling company that has been in business since 2003. We primarily work in the mid peninsula of the bay area. Most of our clientele are very educated captains of industry. This group is still the target client.
I had my logo designed by Mint Easel a few years ago and I do like it, I like the orange and black or orange a blue. I don’t have a lot of content on hand as far as professional photographs.
Number of pages not sure and are open to: design pages vs full function website
I think what I am after is a web presence that will seal the deal as we are getting high referrals from past clients.
Construction
1 page

```html
<!DOCTYPE html>
<html lang="en">
<head>
<meta charset="utf-8">
<title>Quenbrick Hall Remodeling</title>
<link rel="stylesheet" href="https://fonts.googleapis.com/css2?family=Exo+2:wght@500;600;700&family=Open+Sans:wght@400;600;700&display=swap">
<style>
:root{
  --orange:#f26a0f;
  --orange-dark:#d95a05;
  --ink:#1b1b1b;
  --text:#444;
  --muted:#777;
  --grey-band:#ebebeb;
  --footer:#141414;
  --footer-bar:#0a0a0a;
  --white:#fff;
  --rule:#c9c9c9;
  --map-light:#e6e0d4;
  --map-cool:#d5d9dc;
}
*{box-sizing:border-box;margin:0;padding:0}
html,body{width:1200px;height:2740px;overflow:hidden;background:var(--white)}
body{position:relative;font-family:"Open Sans",Arial,sans-serif;color:var(--text)}
.abs{position:absolute}

/* header */
.site-header{left:0;top:0;width:1200px;height:92px;background:var(--white);z-index:5}
.brand{left:88px;top:22px;display:flex;align-items:center;gap:12px}
.brand-square{width:44px;height:44px;background:var(--ink)}
.brand-name{font-family:"Exo 2",sans-serif;font-weight:700;font-size:19px;line-height:1.05;color:var(--orange);letter-spacing:.5px}
.main-nav{right:88px;top:0;height:92px;display:flex;gap:40px;align-items:center}
.main-nav a{font-family:"Exo 2",sans-serif;font-weight:600;font-size:13px;color:#333;text-decoration:none;height:92px;display:flex;align-items:center;position:relative}
.main-nav a.active{color:var(--orange)}
.main-nav a.active::after{content:"";position:absolute;left:-6px;right:-6px;bottom:0;height:3px;background:var(--orange)}

/* hero */
.hero-edge{left:0;top:92px;width:1200px;height:540px;background:var(--orange);clip-path:polygon(0 0,100% 0,100% 530px,50% 436px,0 540px)}
.hero-photo{left:0;top:92px;width:1200px;height:530px;clip-path:polygon(0 0,100% 0,100% 518px,50% 424px,0 528px);
  background:linear-gradient(90deg,rgba(20,20,20,.55),rgba(20,20,20,.35) 50%,rgba(20,20,20,.6)),linear-gradient(180deg,#8a8d90 0%,#6c6a66 45%,#4a4540 100%)}
.hero-copy{left:0;top:230px;width:1200px;text-align:center;color:var(--white)}
.hero-title{font-family:"Exo 2",sans-serif;font-weight:700;font-size:36px;letter-spacing:.5px}
.hero-title .mark{background:var(--orange);padding:0 6px}
.hero-sub{margin-top:14px;font-size:15.5px;letter-spacing:1px;color:#e6e6e6}
.hero-contacts{margin-top:16px;display:flex;justify-content:center;gap:32px;font-size:15px}
.hero-contacts span{display:flex;align-items:center;gap:10px}

/* section headings */
.section-head{left:0;width:1200px;text-align:center}
.head-rule{position:relative;width:482px;height:20px;margin:0 auto}
.head-rule::before{content:"";position:absolute;left:0;right:0;top:10px;height:1px;background:var(--rule)}
.head-rule::after{content:"";position:absolute;left:232px;top:1px;width:18px;height:18px;background:var(--ink);box-shadow:0 0 0 6px var(--white)}
.on-grey .head-rule::after{box-shadow:0 0 0 6px var(--grey-band)}
.section-title{margin-top:10px;font-family:"Exo 2",sans-serif;font-weight:700;font-size:33px;color:var(--ink);letter-spacing:.3px}

.intro-copy{left:130px;top:700px;width:940px;text-align:center;font-size:13.5px;line-height:22px;color:var(--text)}
.intro-copy p+p{margin-top:22px}

/* projects */
.project-band{left:0;top:898px;width:1200px;height:1016px;background:var(--grey-band);clip-path:polygon(50% 0,100% 103px,100% 100%,50% 910px,0 100%,0 103px)}
.project-grid{left:0;top:1090px}

/* testimonial */
.quote-mark{left:216px;top:1930px;font-family:Georgia,serif;font-size:200px;line-height:1;color:#e6e6e6;font-weight:700}
.quote-text{left:290px;top:2030px;width:680px;text-align:center;font-size:13px;line-height:22px;color:var(--text)}
.avatar{left:551px;top:2099px;width:96px;height:96px;border-radius:50%;border:3px solid var(--orange);padding:5px;background:var(--white)}
.avatar-fill{width:100%;height:100%;border-radius:50%;background:radial-gradient(circle at 50% 40%,#d8d8d8,#9a9a9a)}
.person{left:0;top:2215px;width:1200px;text-align:center}
.person-name{font-weight:700;font-size:20px;color:var(--ink);letter-spacing:.5px}
.person-role{font-size:11.5px;color:var(--muted);margin-top:2px}
.dots{left:568px;top:2274px;display:flex;gap:4px}
.dots i{width:9px;height:9px;border-radius:50%;background:var(--ink)}
.dots i.on{background:var(--orange)}

/* footer */
.footer-edge{left:0;top:2319px;width:1200px;height:421px;background:var(--orange);clip-path:polygon(50% 0,100% 110px,100% 100%,0 100%,0 110px)}
.footer-body{left:0;top:2329px;width:1200px;height:411px;background:var(--footer);clip-path:polygon(50% 0,100% 110px,100% 100%,0 100%,0 110px)}
.footer-mark{left:0;top:2366px;width:1200px;text-align:center;font-family:"Exo 2",sans-serif;font-weight:700;font-size:18px;color:var(--white);letter-spacing:1px}
.footer-col{top:2450px;color:#cfcfcf}
.footer-col h3{font-family:"Exo 2",sans-serif;font-weight:500;font-size:17px;color:var(--white);letter-spacing:.5px;padding-bottom:10px;border-bottom:1px solid #3a3a3a;width:140px}
.quick-links{list-style:none;margin-top:16px}
.quick-links li{font-size:11px;color:#e0e0e0;height:31px;display:flex;align-items:center;gap:12px}
.quick-links li::before{content:"";border-left:5px solid var(--orange);border-top:3px solid transparent;border-bottom:3px solid transparent}
.map{margin-top:20px;width:234px;height:155px;background:linear-gradient(180deg,var(--map-light) 0%,var(--map-cool) 100%)}
.contact-list{margin-top:16px;width:220px}
.contact-row{display:flex;gap:12px;align-items:flex-start;margin-bottom:14px}
.c-icon{flex:none;width:24px;height:24px;border-radius:50%;background:var(--orange);display:flex;align-items:center;justify-content:center}
.contact-row strong{display:block;font-size:12px;color:var(--white)}
.contact-row small{display:block;font-size:10.5px;line-height:14px;color:#bdbdbd;margin-top:3px}
.contact-row .big{font-size:18px;color:var(--white);line-height:24px}
.contact-row .mail{font-size:11.5px;color:#e0e0e0;line-height:24px}
.socials{margin-top:12px;display:flex;gap:6px}
.socials i{width:22px;height:22px;border-radius:50%;background:#8c8c8c}
.newsletter{margin-top:14px}
.email-field{margin-top:14px;width:186px;height:30px;background:var(--white);border-radius:2px;font-size:10px;color:#aaa;padding:0 8px;line-height:30px}
.submit{margin-top:17px;width:75px;height:22px;background:var(--orange);color:var(--white);font-size:11px;font-weight:700;text-align:center;line-height:22px}
.copyright{left:0;top:2699px;width:1200px;height:41px;background:var(--footer-bar);text-align:center;line-height:41px;font-size:11px;color:#9a9a9a}
</style>
</head>
<body>

<header class="site-header abs">
  <div class="brand abs">
    <div class="brand-square"></div>
    <div class="brand-name">QUENBRICK HALL<br>REMODELING</div>
  </div>
  <nav class="main-nav abs">
    <a class="active">HOME</a><a>ABOUT US</a><a>GALLERY</a><a>TESTIMONIALS</a><a>CONTACT US</a>
  </nav>
</header>

<div class="hero-edge abs"></div>
<div class="hero-photo abs" role="img" aria-label="Builder in a hard hat showing a couple around a large house under construction"></div>
<div class="hero-copy abs">
  <h1 class="hero-title">WE ARE A <span class="mark">HIGH END</span> CONSTRUCTION</h1>
  <p class="hero-sub">REMODELING COMPANY THAT HAS BEEN IN BUSINESS SINCE 2003</p>
  <div class="hero-contacts">
    <span><svg width="18" height="18" viewBox="0 0 24 24"><path d="M6.6 10.8a15 15 0 0 0 6.6 6.6l2.2-2.2a1 1 0 0 1 1-.25 11.4 11.4 0 0 0 3.6.57 1 1 0 0 1 1 1V20a1 1 0 0 1-1 1A17 17 0 0 1 3 4a1 1 0 0 1 1-1h3.5a1 1 0 0 1 1 1c0 1.25.2 2.45.57 3.6a1 1 0 0 1-.25 1z" fill="none" stroke="#f26a0f" stroke-width="2"/></svg>hello@quenbrickhall.com</span>
    <span><svg width="18" height="16" viewBox="0 0 24 20"><rect x="1" y="2" width="22" height="16" fill="none" stroke="#f26a0f" stroke-width="2"/><path d="M1 3l11 8 11-8" fill="none" stroke="#f26a0f" stroke-width="2"/></svg>415.555.0182</span>
  </div>
</div>

<section>
  <div class="section-head abs" style="top:604px">
    <div class="head-rule"></div>
    <h2 class="section-title">WHY CHOOSE QUENBRICK HALL</h2>
  </div>
  <div class="intro-copy abs">
    <p>Lorem Ipsum has been the industry's standard dummy text ever since the 1500s, when an unknown printer took a galley of type and scrambled it to make a type specimen book. It has survived not only five centuries, but also the leap into electronic typesetting, remaining essentially unchanged.</p>
    <p>Lorem Ipsum has been the industry's standard dummy text ever since the 1500s, when an unknown printer took a galley of type and scrambled it to make a type specimen book.</p>
  </div>
</section>

<section>
  <div class="project-band abs"></div>
  <div class="section-head on-grey abs" style="top:982px">
    <div class="head-rule"></div>
    <h2 class="section-title">CURRENT PROJECT</h2>
  </div>
  <svg class="project-grid abs" width="1200" height="650" viewBox="0 0 1200 650">
    <defs>
      <linearGradient id="g-bed" x1="0" y1="0" x2="0" y2="1"><stop offset="0" stop-color="#c9b89a"/><stop offset="1" stop-color="#6b4a30"/></linearGradient>
      <linearGradient id="g-tile" x1="0" y1="0" x2="0" y2="1"><stop offset="0" stop-color="#d9cbb8"/><stop offset="1" stop-color="#5a4a40"/></linearGradient>
      <linearGradient id="g-view" x1="0" y1="0" x2="0" y2="1"><stop offset="0" stop-color="#b7c2c6"/><stop offset="1" stop-color="#8a6a44"/></linearGradient>
      <linearGradient id="g-island" x1="0" y1="0" x2="0" y2="1"><stop offset="0" stop-color="#a8b0b0"/><stop offset="1" stop-color="#4a3e34"/></linearGradient>
      <linearGradient id="g-bath" x1="0" y1="0" x2="0" y2="1"><stop offset="0" stop-color="#d6cbb5"/><stop offset="1" stop-color="#9c8a70"/></linearGradient>
      <linearGradient id="g-white" x1="0" y1="0" x2="0" y2="1"><stop offset="0" stop-color="#e6e6e2"/><stop offset="1" stop-color="#3a3d48"/></linearGradient>
      <linearGradient id="g-wine" x1="0" y1="0" x2="0" y2="1"><stop offset="0" stop-color="#d4cdc3"/><stop offset="1" stop-color="#3a2a22"/></linearGradient>
      <linearGradient id="g-shower" x1="0" y1="0" x2="0" y2="1"><stop offset="0" stop-color="#8fa196"/><stop offset="1" stop-color="#cfd0cc"/></linearGradient>
      <linearGradient id="g-galley" x1="0" y1="0" x2="0" y2="1"><stop offset="0" stop-color="#d8c7b0"/><stop offset="1" stop-color="#7a5638"/></linearGradient>
    </defs>
    <g role="img" aria-label="Bedroom with a wooden bed"><polygon points="358,16 465,75 465,191 358,250 251,191 251,75" fill="url(#g-bed)"/></g>
    <g role="img" aria-label="Kitchen range with patterned tile backsplash"><polygon points="599,16 706,75 706,191 599,250 492,191 492,75" fill="url(#g-tile)"/></g>
    <g role="img" aria-label="Kitchen with a large window view"><polygon points="840,16 947,75 947,191 840,250 733,191 733,75" fill="url(#g-view)"/></g>
    <g role="img" aria-label="Stone kitchen island countertop"><polygon points="234,204 341,263 341,379 234,438 127,379 127,263" fill="url(#g-island)"/></g>
    <polygon points="478,204 585,263 585,379 478,438 371,379 371,263" fill="#f26a0f" stroke="#3a3a3a" stroke-width="4"/>
    <rect x="431" y="300" width="36" height="36" fill="none" stroke="#fff" stroke-width="1.5"/>
    <circle cx="447" cy="316" r="7" fill="none" stroke="#fff" stroke-width="2.5"/><line x1="452" y1="321" x2="458" y2="327" stroke="#fff" stroke-width="3"/>
    <rect x="488" y="300" width="36" height="36" fill="none" stroke="#fff" stroke-width="1.5"/>
    <rect x="496" y="313" width="12" height="7" rx="3.5" transform="rotate(45 502 316)" fill="none" stroke="#fff" stroke-width="2.2"/>
    <rect x="504" y="317" width="12" height="7" rx="3.5" transform="rotate(45 510 320)" fill="none" stroke="#fff" stroke-width="2.2"/>
    <g role="img" aria-label="Bathroom vanity with a stone vessel sink"><polygon points="720,204 827,263 827,379 720,438 613,379 613,263" fill="url(#g-bath)"/></g>
    <g role="img" aria-label="White kitchen with dining chairs"><polygon points="962,204 1069,263 1069,379 962,438 855,379 855,263" fill="url(#g-white)"/></g>
    <g role="img" aria-label="Counter with built-in wine rack"><polygon points="358,396 465,455 465,571 358,630 251,571 251,455" fill="url(#g-wine)"/></g>
    <g role="img" aria-label="Tiled shower with fixtures"><polygon points="599,396 706,455 706,571 599,630 492,571 492,455" fill="url(#g-shower)"/></g>
    <g role="img" aria-label="Kitchen with wood cabinets and steel refrigerator"><polygon points="840,396 947,455 947,571 840,630 733,571 733,455" fill="url(#g-galley)"/></g>
  </svg>
</section>

<section>
  <div class="section-head abs" style="top:1916px">
    <div class="head-rule"></div>
    <h2 class="section-title">CURRENT PROJECT</h2>
  </div>
  <div class="quote-mark abs">&ldquo;</div>
  <p class="quote-text abs">Nounc at pretium est curabitur commodo leac est venenatis egestas sed aliquet auguevelit. Lorem ipsum dolor sit amet, consectetur adipiscing elit. Vivamus ac luctus ligula. Phasellus a ligula blandit.</p>
  <div class="avatar abs"><div class="avatar-fill" role="img" aria-label="Portrait of the client giving the testimonial"></div></div>
  <div class="person abs">
    <div class="person-name">Marten Oderwald</div>
    <div class="person-role">Site Builder</div>
  </div>
  <div class="dots abs"><i class="on"></i><i></i><i></i><i></i><i></i></div>
</section>

<footer>
  <div class="footer-edge abs"></div>
  <div class="footer-body abs"></div>
  <div class="footer-mark abs">QUENBRICK HALL</div>

  <div class="footer-col abs" style="left:117px">
    <h3>QUICK LINKS</h3>
    <ul class="quick-links">
      <li>HOME</li><li>ABOUT US</li><li>GALLERY</li><li>TESTIMONIALS</li><li>CONTACT US</li>
    </ul>
  </div>

  <div class="footer-col abs" style="left:323px">
    <h3>LOCATION MAP</h3>
    <div class="map" role="img" aria-label="Street map showing the office location"></div>
  </div>

  <div class="footer-col abs" style="left:621px">
    <h3 style="width:180px">CONTACT DETAILS</h3>
    <div class="contact-list">
      <div class="contact-row">
        <span class="c-icon"><svg width="10" height="14" viewBox="0 0 10 14"><path d="M5 0a5 5 0 0 1 5 5c0 3.5-5 9-5 9S0 8.5 0 5a5 5 0 0 1 5-5z" fill="#fff"/><circle cx="5" cy="5" r="2" fill="#f26a0f"/></svg></span>
        <div><strong>Quenbrick Hall Remodeling</strong><small>Diam nummy Rich,<br>euiloumn tincidunt ut laor<br>laoreet dolore magna<br>123456</small></div>
      </div>
      <div class="contact-row">
        <span class="c-icon"><svg width="12" height="12" viewBox="0 0 24 24"><path d="M6.6 10.8a15 15 0 0 0 6.6 6.6l2.2-2.2a1 1 0 0 1 1-.25 11.4 11.4 0 0 0 3.6.57 1 1 0 0 1 1 1V20a1 1 0 0 1-1 1A17 17 0 0 1 3 4a1 1 0 0 1 1-1h3.5a1 1 0 0 1 1 1c0 1.25.2 2.45.57 3.6a1 1 0 0 1-.25 1z" fill="#fff"/></svg></span>
        <span class="big">650-555-0147</span>
      </div>
      <div class="contact-row">
        <span class="c-icon"><svg width="12" height="10" viewBox="0 0 24 20"><rect x="1" y="2" width="22" height="16" fill="#fff"/><path d="M1 3l11 8 11-8" fill="none" stroke="#f26a0f" stroke-width="2"/></svg></span>
        <span class="mail">info@quenbrickhall.com</span>
      </div>
    </div>
  </div>

  <div class="footer-col abs" style="left:882px">
    <h3>FOLLOW US</h3>
    <div class="socials"><i></i><i></i><i></i><i></i><i></i><i></i></div>
    <h3 class="newsletter">NEWSLETTER</h3>
    <div class="email-field">Email Address</div>
    <div class="submit">SUBMIT</div>
  </div>

  <div class="copyright abs">Copyright &copy; 2016 Quenbrick Hall Remodeling, Inc. All rights reserved.</div>
</footer>

</body>
</html>
```